Realtor Business Card for Marisol!

I sell real estate in a tropical location near the ocean, beaches and palm trees.

The homes are higher end, luxury. I want a card that is professional and attention-grabbing. In a sea full of competition, I need to stand out! I don't want the run-of-the mill card that looks like everyone else's with a different name. I want people to say "wow!".
Updates

Project Deadline Extended Reason: I have a little more time that originally anticipated. Added Friday, July 7, 2017

Target Market(s)

All.

Industry/Entity Type

Real Estate Agent

Contact Information for Business Card

Name: Marisol Vankeer-Odham
Email: marisol@harborview-estates.example
Website: www.harborviewestates.example
Phone: 555.418.7263

Font styles to use
Serif

Colors

Designer to choose colors to be used in the design.

Requirements
Must have
• All attachments.
Nice to have
• Gold edges
• Transparent card
• Unique shape

```html
<!DOCTYPE html>
<html lang="en">
<head>
<meta charset="utf-8">
<title>Harborview Estates — Business Card</title>
<link href="https://fonts.googleapis.com/css2?family=Roboto:wght@400;700&family=Dancing+Script:wght@500&display=swap" rel="stylesheet">
<style>
  :root {
    --backdrop: #3a322e;
    --card: #1e2023;
    --card-edge: #b8863b;
    --gold: #b8952e;
    --silver: #d9d9d9;
    --text-light: #e8e8e8;
    --rule: #cfcfcf;
    --photo-top: #d8d8d8;
    --photo-bottom: #a7927e;
  }
  * { box-sizing: border-box; margin: 0; padding: 0; }
  html, body {
    width: 1200px; height: 769px; overflow: hidden;
    background: var(--backdrop);
    font-family: "Roboto", Arial, sans-serif;
  }
  .canvas { position: relative; width: 1200px; height: 769px; }

  .card {
    position: absolute; top: 227px;
    width: 540px; height: 315px;
    background: var(--card);
    border-radius: 4px;
    box-shadow: 0 0 0 2px var(--card-edge), 0 14px 30px rgba(0,0,0,.45);
    overflow: hidden;
  }
  .card--front { left: 40px; }
  .card--back { left: 620px; }

  /* Front */
  .agent-photo {
    position: absolute; left: 30px; top: 50px;
    width: 130px; height: 150px; border-radius: 14px;
    background: linear-gradient(170deg, var(--photo-top) 0%, var(--photo-top) 45%, var(--photo-bottom) 100%);
  }
  .brand {
    position: absolute; display: flex; align-items: center; gap: 10px;
    font-weight: 700; white-space: nowrap;
  }
  .brand__dot { border-radius: 50%; flex: none; }
  .card--front .brand { left: 236px; top: 40px; font-size: 24px; color: var(--gold); }
  .card--front .brand__dot { width: 20px; height: 20px; background: var(--gold); }
  .divider {
    position: absolute; left: 180px; top: 110px;
    width: 330px; height: 1px; background: var(--rule);
  }
  .agent-name {
    position: absolute; left: 30px; top: 212px;
    font-size: 20px; font-weight: 700; letter-spacing: .3px;
    color: var(--gold); text-transform: uppercase;
  }
  .name-rule {
    position: absolute; left: 30px; top: 242px;
    width: 210px; height: 1px; background: var(--rule);
  }
  .contact-list {
    position: absolute; left: 30px; top: 249px; list-style: none;
  }
  .contact-list li {
    display: flex; align-items: center; gap: 9px;
    height: 18px; font-size: 13px; color: var(--text-light);
  }
  .contact-list svg { width: 12px; height: 12px; fill: var(--gold); flex: none; }

  /* Back */
  .badges {
    position: absolute; right: 22px; top: 16px; display: flex; gap: 6px;
  }
  .badge { width: 20px; height: 16px; border: 1.5px solid var(--silver); border-radius: 2px; }
  .badge--wide { width: 30px; }
  .card--back .brand {
    left: 0; right: 0; top: 112px; justify-content: center;
    font-size: 36px; color: var(--silver);
  }
  .card--back .brand__dot { width: 28px; height: 28px; background: var(--silver); }
  .tagline {
    position: absolute; left: 0; right: 0; top: 196px; text-align: center;
    font-family: "Dancing Script", cursive; font-size: 26px; color: var(--gold);
  }
</style>
</head>
<body>
<main class="canvas">

  <section class="card card--front" aria-label="Card front">
    <div class="agent-photo" role="img" aria-label="Portrait photo of the agent"></div>
    <div class="brand"><span class="brand__dot"></span><span class="brand__name">Harborview Estates</span></div>
    <div class="divider"></div>
    <h1 class="agent-name">Marisol Vankeer-Odham</h1>
    <div class="name-rule"></div>
    <ul class="contact-list">
      <li>
        <svg viewBox="0 0 24 24" aria-hidden="true"><path d="M6.6 10.8a15.1 15.1 0 0 0 6.6 6.6l2.2-2.2a1 1 0 0 1 1-.25 11.4 11.4 0 0 0 3.6.57 1 1 0 0 1 1 1V20a1 1 0 0 1-1 1A17 17 0 0 1 3 4a1 1 0 0 1 1-1h3.5a1 1 0 0 1 1 1c0 1.25.2 2.45.57 3.57a1 1 0 0 1-.25 1z"/></svg>
        555.418.7263
      </li>
      <li>
        <svg viewBox="0 0 24 24" aria-hidden="true"><path d="M2 5h20v14H2z M2 5l10 7 10-7" /></svg>
        marisol@harborview-estates.example
      </li>
      <li>
        <svg viewBox="0 0 24 24" aria-hidden="true"><circle cx="12" cy="12" r="10"/></svg>
        www.harborviewestates.example
      </li>
    </ul>
  </section>

  <section class="card card--back" aria-label="Card back">
    <div class="badges">
      <span class="badge"></span>
      <span class="badge"></span>
      <span class="badge badge--wide"></span>
    </div>
    <div class="brand"><span class="brand__dot"></span><span class="brand__name">Harborview Estates</span></div>
    <p class="tagline">Stay by the Shore...</p>
  </section>

</main>
</body>
</html>
```